Awesome photographers card for an awesome new business

Double sided business card Black background and silver logo in middle on one side. Details on otherside. please keep it simple

Industry/Entity Type

Photographer

Contact Information for Business Card

Colin Fairweather
0452816307
ColinFairweatherPhotography57@mailvane.com
www.ColinFairweatherPhotography.com.au
Instagram _Colin_fairweather

Requirements
Must have
• My logo in Silver
• please use instagram logo instead of "Instagram"

```html
<!DOCTYPE html>
<html lang="en">
<head>
<meta charset="utf-8">
<title>Colin Fairweather Photography – Business Card</title>
<link href="https://fonts.googleapis.com/css2?family=Montserrat:wght@400;500&display=swap" rel="stylesheet">
<style>
  :root {
    --backdrop: #2b2b2b;
    --card: #0e0e0e;
    --card-edge: #1c1c1c;
    --silver: #c9c9c9;
    --white: #f2f2f2;
    --divider: #6a6a6a;
  }
  * { margin: 0; padding: 0; box-sizing: border-box; }
  html, body {
    width: 1200px; height: 930px; overflow: hidden;
    background: var(--backdrop);
    font-family: "Montserrat", sans-serif;
  }
  .canvas {
    position: relative; width: 1200px; height: 930px;
    display: flex; flex-direction: column; align-items: center; justify-content: center; gap: 40px;
  }
  .card {
    width: 700px; height: 400px;
    background: linear-gradient(135deg, #141414 0%, var(--card) 60%, #0a0a0a 100%);
    border: 1px solid var(--card-edge);
    box-shadow: 0 12px 30px rgba(0,0,0,0.45);
    position: relative;
  }
  /* Front */
  .card--front { display: flex; align-items: center; justify-content: center; }
  .brand-mark { display: flex; align-items: center; gap: 14px; }
  .brand-mark__dot {
    width: 14px; height: 14px; border-radius: 50%; background: var(--silver);
  }
  .brand-mark__name {
    color: var(--silver); font-weight: 500; font-size: 30px; letter-spacing: 1px;
  }
  /* Back */
  .card--back { display: flex; align-items: center; }
  .back__brand {
    width: 290px; display: flex; justify-content: center;
  }
  .back__brand-name {
    color: var(--white); font-weight: 500; font-size: 24px; letter-spacing: 0.5px; text-align: center; line-height: 1.25;
  }
  .back__divider {
    width: 1px; height: 130px; background: var(--divider);
  }
  .back__details { padding-left: 26px; }
  .back__name {
    color: var(--white); font-weight: 500; font-size: 15px; letter-spacing: 3px; text-transform: uppercase;
    margin-bottom: 16px;
  }
  .contact-list { list-style: none; }
  .contact-list__item {
    display: flex; align-items: center; gap: 12px;
    color: var(--white); font-weight: 400; font-size: 12.5px; line-height: 1; margin-bottom: 9px;
  }
  .contact-list__icon { width: 12px; height: 12px; flex: none; }
  .contact-list__dot { width: 10px; height: 10px; margin: 0 1px; border-radius: 50%; background: var(--white); flex: none; }
</style>
</head>
<body>
<main class="canvas">
  <section class="card card--front" aria-label="Card front">
    <div class="brand-mark">
      <span class="brand-mark__dot"></span>
      <span class="brand-mark__name">Colin Fairweather</span>
    </div>
  </section>

  <section class="card card--back" aria-label="Card back">
    <div class="back__brand">
      <span class="back__brand-name">Colin Fairweather</span>
    </div>
    <div class="back__divider"></div>
    <div class="back__details">
      <p class="back__name">Colin Fairweather</p>
      <ul class="contact-list">
        <li class="contact-list__item">
          <svg class="contact-list__icon" viewBox="0 0 24 24" fill="#f2f2f2"><path d="M6.6 10.8a15.2 15.2 0 0 0 6.6 6.6l2.2-2.2a1 1 0 0 1 1-.25 11.4 11.4 0 0 0 3.6.57 1 1 0 0 1 1 1V20a1 1 0 0 1-1 1A17 17 0 0 1 3 4a1 1 0 0 1 1-1h3.5a1 1 0 0 1 1 1c0 1.25.2 2.45.57 3.6a1 1 0 0 1-.25 1z"/></svg>
          0452816307
        </li>
        <li class="contact-list__item">
          <svg class="contact-list__icon" viewBox="0 0 24 24" fill="#f2f2f2"><path d="M2 5h20v14H2z M2 5l10 8 10-8" /><path d="M2 5l10 8 10-8" fill="none" stroke="#0e0e0e" stroke-width="2"/></svg>
          ColinFairweatherPhotography57@mailvane.com
        </li>
        <li class="contact-list__item">
          <svg class="contact-list__icon" viewBox="0 0 24 24" fill="none" stroke="#f2f2f2" stroke-width="2"><circle cx="12" cy="12" r="10"/><path d="M2 12h20M12 2c3 3 3 17 0 20M12 2c-3 3-3 17 0 20"/></svg>
          www.ColinFairweatherPhotography.com.au
        </li>
        <li class="contact-list__item">
          <span class="contact-list__dot"></span>
          _Colin_fairweather
        </li>
      </ul>
    </div>
  </section>
</main>
</body>
</html>
```